Valbrook Data Works

Our company is about IT hardwares and IT solutions. IT hardware such as PC, RAMS, storage and servers. IT solutions such as project management, BA. We are also selling new technology too.

Target Market(s)

Consumer, Small to Medium Business, Corporate

Requirements
Must have
• The business card must have the following:
• Name:
• Title:
• Contact Number:
• Email address:
• Website:
• Color: Must match the logo color upgrade

```html
<!DOCTYPE html>
<html lang="en">
<head>
<meta charset="utf-8">
<title>Valbrook Data Works — Business Card</title>
<link href="https://fonts.googleapis.com/css2?family=Saira+Semi+Condensed:wght@600;700&family=Montserrat:wght@400;500&display=swap" rel="stylesheet">
<style>
  :root {
    --bg: #e2e2e2;
    --card: #f7f7f7;
    --ink: #4f4f4f;
    --ink-dark: #1f1f1f;
    --accent: #d57f26;
    --rule: #5a5a5a;
  }
  * { box-sizing: border-box; margin: 0; padding: 0; }
  html, body { width: 1200px; height: 864px; overflow: hidden; }
  body {
    background: var(--bg);
    display: flex;
    align-items: center;
    justify-content: center;
    gap: 40px;
  }
  .card {
    position: relative;
    width: 540px;
    height: 309px;
    background: var(--card);
    box-shadow: 0 2px 6px rgba(0,0,0,.12);
    overflow: hidden;
  }
  .brand {
    display: flex;
    align-items: center;
    gap: 8px;
    font-family: "Saira Semi Condensed", sans-serif;
    font-weight: 700;
    color: var(--ink);
    font-size: 26px;
    letter-spacing: .5px;
    text-transform: uppercase;
    white-space: nowrap;
  }
  .brand-mark {
    width: 14px; height: 14px;
    background: var(--accent);
    flex: none;
  }

  /* Front */
  .card-front .brand { position: absolute; left: 118px; top: 56px; }
  .card-front .divider {
    position: absolute; left: 0; top: 104px;
    width: 340px; height: 2px; background: var(--rule);
  }
  .holder { position: absolute; left: 30px; top: 116px; }
  .holder-name {
    font-family: "Montserrat", sans-serif;
    font-weight: 500;
    font-size: 19px;
    color: var(--ink);
    letter-spacing: .5px;
  }
  .holder-title {
    font-family: "Montserrat", sans-serif;
    font-size: 13px;
    color: var(--accent);
    letter-spacing: .5px;
  }
  .contacts {
    position: absolute; left: 30px; top: 178px;
    list-style: none;
    display: flex; flex-direction: column; gap: 9px;
  }
  .contact {
    display: flex; align-items: center; gap: 12px;
    font-family: "Montserrat", sans-serif;
    font-size: 15px;
    color: var(--ink-dark);
    letter-spacing: .4px;
  }
  .contact-icon {
    width: 17px; height: 17px;
    background: var(--accent);
    display: flex; align-items: center; justify-content: center;
    flex: none;
  }
  .contact-icon svg { width: 11px; height: 11px; }

  /* Back */
  .card-back .brand { position: absolute; left: 64px; top: 118px; }
  .card-back .accent-line {
    position: absolute; left: 62px; top: 162px;
    width: 440px; height: 3px; background: var(--accent);
  }
</style>
</head>
<body>
  <section class="card card-front" aria-label="Business card front">
    <div class="brand"><span class="brand-mark"></span>Valbrook Data Works</div>
    <div class="divider"></div>
    <div class="holder">
      <p class="holder-name">MARCUS HALE</p>
      <p class="holder-title">MANAGER</p>
    </div>
    <ul class="contacts">
      <li class="contact">
        <span class="contact-icon">
          <svg viewBox="0 0 12 12"><path d="M3 1 L5 3.5 L4 4.8 Q5 7 7.2 8 L8.5 7 L11 9 L9.8 11 Q4 10.5 1 3.2 Z" fill="#fff"/></svg>
        </span>+1-555-204-7718
      </li>
      <li class="contact">
        <span class="contact-icon">
          <svg viewBox="0 0 12 12"><rect x="1" y="2.5" width="10" height="7" fill="none" stroke="#fff" stroke-width="1.2"/><path d="M1 2.5 L6 7 L11 2.5" fill="none" stroke="#fff" stroke-width="1.2"/></svg>
        </span>marcus@valbrookdata.com
      </li>
      <li class="contact">
        <span class="contact-icon">
          <svg viewBox="0 0 12 12"><circle cx="6" cy="6" r="4.8" fill="none" stroke="#fff" stroke-width="1.1"/><ellipse cx="6" cy="6" rx="2" ry="4.8" fill="none" stroke="#fff" stroke-width="1"/><path d="M1.2 6 H10.8" stroke="#fff" stroke-width="1"/></svg>
        </span>www.valbrookdata.com
      </li>
    </ul>
  </section>

  <section class="card card-back" aria-label="Business card back">
    <div class="brand"><span class="brand-mark"></span>Valbrook Data Works</div>
    <div class="accent-line"></div>
  </section>
</body>
</html>
```